Apartment Complex in Southeastern US needs new signage & identity!

Need a design for a physical sign/logo & signage for a 28 unit apartment complex in West Columbia, South Carolina, USA.

These are properties that, in their market , I would describe as "affordable." They are no-frills accommodations that are safe, clean and inexpensive.

The sign I want foremost is something that will be free-standing (not attached). Approximate measurements of the main finished sign should be about 4' x 6' (but really this is just an aspect ratio of course.)

Ideally also want to have smaller signs of a coordinated design created to denote the building number (maybe even on each door), but that is a secondary task. You'll get an idea for how ugly the current numbering and signage looks in some of the attached photos. Some of the photos also came from the old Chatterly page of the prior management company. (This project could also possibly expand into creating new assets for taking over and rebranding that chatterly page.)

The apartments are currently called "Brackwell Properties" but frankly speaking I despise this name and want to change (rebrand) it. As the new owner I am thinking to change the name:

Sign should basically say something like the following...

Hollin Apartments
1 & 2 Bedroom Units
3817 Dunmore Creek Rd.
Professionally Managed by
Ferrow Properties: (XXX)XXX-XXXX

"Managed by" part should be detachable. For instance if I ever need to change management companies, I'd just want to be able to swap out that part of the sign, not the whole thing, of course.

Another consideration is that it would be good if there could be a "units available" or "move-in-special" part that could be attached to the top based on the property's status.

I think that earth colors are favorable and nice looking for what this is and where it is located.... greens/browns/tans/greys, etc.

Many similar signs I've seen online and in person have an this Fair Tenancy Pledge logo on it (one of the example signs in the attached images appears this way). I may want to have that appear on the sign -- I'm not yet decided.

I'm attaching some logos of similar signs, as well as some photos of the property itself. You can probably also find more information and photos (Mapvista Road Lens.)

I can answer any question or inquiry you might have in pretty short time.

Target Market(s)

- Low-Mid income singles & families in the Southeast US looking for safe & affordable housing

Industry/Entity Type

Apartment

Requirements
Must have
• - A design proposal for an outdoor sign
• - Design for sign should have some 'detachable' parts for the management company, and to indicate whether units are available and
Nice to have
• - "Earthy" colors: tans/browns/greens etc. seem like it might be nice. (The region, [US postal code 28413] has lots and lots of pine trees.)
Should not have
• No comic sans! :)

```html
<!DOCTYPE html>
<html lang="en">
<head>
<meta charset="utf-8">
<title>Apartments Sign</title>
<link rel="stylesheet" href="https://fonts.googleapis.com/css2?family=Cinzel:wght@500&family=Kalam:wght@400&family=Arimo:wght@400;700&family=Libre+Baskerville:wght@400;700&display=swap">
<style>
  :root {
    --teal: #0f6e63;
    --gold: #f2b450;
    --bark: #8a5a24;
    --panel: #eef7ef;
    --ink: #1d2a1c;
    --address: #8a6a05;
    --green: #3a8a4f;
    --logo-green: #2aa86a;
    --access-blue: #1a58a8;
    --slot-blue: #1f4fa0;
    --grey-line: #6d6d6d;
  }
  html, body { margin: 0; padding: 0; overflow: hidden; background: #ffffff; }
  .canvas { position: relative; width: 1200px; height: 1050px; overflow: hidden; background: #ffffff; }
  .sign-frame { position: absolute; left: 0; top: 0; }

  .brand-card {
    position: absolute; left: 538px; top: 18px; width: 180px; height: 256px;
    border: 2px solid #b7b7b7; box-sizing: border-box; background: #fff;
    display: flex; flex-direction: column; align-items: center; justify-content: center; gap: 18px;
  }
  .brand-mark { width: 70px; height: 70px; background: var(--logo-green); }
  .brand-name {
    font-family: 'Arimo', sans-serif; font-weight: 400; font-size: 19px;
    color: var(--teal); text-align: center; line-height: 1.3; letter-spacing: 1px;
  }

  .units-title {
    position: absolute; left: 200px; width: 840px; top: 432px; text-align: center;
    font-family: 'Cinzel', serif; font-weight: 500; font-size: 50px; letter-spacing: 6px; color: var(--ink);
  }
  .address-plate {
    position: absolute; left: 432px; top: 522px; width: 360px; height: 42px; box-sizing: border-box;
    border: 2px solid #333; border-radius: 4px; background: #fff;
    font-family: 'Kalam', cursive; font-size: 29px; color: var(--address);
    display: flex; align-items: center; justify-content: center; line-height: 1;
  }
  .managed-label {
    position: absolute; left: 256px; width: 710px; top: 609px; text-align: center;
    font-family: 'Arimo', sans-serif; font-size: 34px; color: #1a1a1a;
  }
  .manager-plate {
    position: absolute; left: 256px; top: 653px; width: 710px; height: 62px; box-sizing: border-box;
    border: 1px solid #999; border-radius: 3px;
    background: linear-gradient(#fafafa, #d9d9d9);
    box-shadow: 2px 3px 0 var(--grey-line);
    font-family: 'Libre Baskerville', serif; font-size: 27px; color: #222; letter-spacing: 1px;
    display: flex; align-items: center; justify-content: center;
  }
  .access-badge { position: absolute; left: 198px; top: 734px; }
  .availability-label {
    position: absolute; left: 904px; top: 717px;
    font-family: 'Arimo', sans-serif; font-weight: 700; font-size: 21px; color: #111;
  }
  .availability-slot {
    position: absolute; left: 930px; top: 741px; width: 86px; height: 64px; box-sizing: border-box;
    border: 5px solid var(--slot-blue); border-radius: 6px; background: #fff;
  }
  .zip-code {
    position: absolute; left: 522px; width: 200px; top: 765px; text-align: center;
    font-family: 'Arimo', sans-serif; font-size: 42px; color: #222; letter-spacing: 1px;
  }
  .city-line {
    position: absolute; left: 472px; width: 300px; top: 809px; text-align: center;
    font-family: 'Arimo', sans-serif; font-size: 22px; color: #222;
  }
  .apartments-band {
    position: absolute; left: 474px; top: 860px; width: 304px; height: 44px;
    background: var(--green); color: #fff;
    font-family: 'Libre Baskerville', serif; font-weight: 700; font-size: 42px;
    display: flex; align-items: center; justify-content: center; line-height: 1;
  }
</style>
</head>
<body>
<div class="canvas">
  <div class="brand-card">
    <div class="brand-mark"></div>
    <div class="brand-name">Sorrel Enterprises</div>
  </div>

  <svg class="sign-frame" width="1200" height="1050" viewBox="0 0 1200 1050">
    <defs>
      <linearGradient id="ovalFill" x1="0" y1="0" x2="0" y2="1">
        <stop offset="0" stop-color="#ffffff"/>
        <stop offset="1" stop-color="#dcdcdc"/>
      </linearGradient>
    </defs>
    <!-- roof band -->
    <path d="M165,378 Q620,222 1078,378" fill="none" stroke="var(--teal)" stroke-width="9"/>
    <path d="M185,392 Q620,256 1058,392" fill="none" stroke="var(--gold)" stroke-width="6"/>
    <!-- outer body -->
    <path d="M168,378 L168,843 L1078,843 L1078,378" fill="none" stroke="var(--teal)" stroke-width="9"/>
    <!-- panel -->
    <path d="M185,395 Q620,259 1055,395 L1055,822 L185,822 Z" fill="var(--panel)" stroke="var(--gold)" stroke-width="6"/>
    <!-- eaves -->
    <path d="M245,382 L113,418 L118,442 L245,410 Z" fill="#fff" stroke="var(--teal)" stroke-width="8" stroke-linejoin="miter"/>
    <path d="M995,382 L1128,432 L1122,455 L995,410 Z" fill="#fff" stroke="var(--teal)" stroke-width="8"/>
    <!-- side notches -->
    <path d="M238,380 L255,380 L255,492 L276,492 L276,520 L180,520 L180,492 L238,492 Z" fill="#fff" stroke="var(--bark)" stroke-width="5"/>
    <path d="M985,378 L1002,378 L1002,492 L1078,492 L1078,518 L963,518 L963,492 L985,492 Z" fill="#fff" stroke="var(--bark)" stroke-width="5"/>
    <path d="M182,520 L182,828 L1058,828 L1058,518" fill="none" stroke="var(--teal)" stroke-width="6"/>
    <!-- oval medallion -->
    <ellipse cx="622" cy="832" rx="188" ry="92" fill="url(#ovalFill)" stroke="var(--teal)" stroke-width="8"/>
    <ellipse cx="622" cy="832" rx="178" ry="83" fill="none" stroke="var(--teal)" stroke-width="2"/>
  </svg>

  <div class="units-title">1&amp;2 Bedroom Units</div>
  <div class="address-plate">3817 Dunmore Creek Rd.</div>
  <div class="managed-label">Professionally Managed by:</div>
  <div class="manager-plate">Ferrow Properties: (xxx)xxx-xxxx</div>

  <svg class="access-badge" width="72" height="70" viewBox="0 0 72 70" role="img" aria-label="Accessibility symbol">
    <rect x="1" y="1" width="70" height="68" rx="4" fill="var(--access-blue)" stroke="#fff" stroke-width="2"/>
    <circle cx="30" cy="15" r="5" fill="#fff"/>
    <path d="M30,22 L30,40 L46,40 L52,55" fill="none" stroke="#fff" stroke-width="5" stroke-linecap="round" stroke-linejoin="round"/>
    <path d="M30,30 L42,30" stroke="#fff" stroke-width="4" stroke-linecap="round"/>
    <path d="M22,32 A15,15 0 1 0 44,50" fill="none" stroke="#fff" stroke-width="4"/>
  </svg>

  <div class="availability-label">Available Ap.</div>
  <div class="availability-slot"></div>

  <div class="zip-code">28413</div>
  <div class="city-line">W. Columbia SC</div>
  <div class="apartments-band">Apartments</div>
</div>
</body>
</html>
```